GreenGlider Powerpoint Template Project

Develop a custom .ppt template that effectively communicates the GreenGlider value proposition and can be tailored for our different audiences: retail partnerships, strategic partnerships, institutional funding and end customers. Our studies have shown a massive improvement in putting effectiveness when using the GreenGlider solution for just 3-5 minutes per day. We would like this dramatic result to be front and center of our value proposition. Putting makes up a huge percentage of a golfer's score (over 40%), but it's widely known that the average golfer spends very little time practicing putting. Reasons for this are reported as: "it's boring"; "tedious"; "it's easy, so I don't need to practice as much"; "I'd rather spend my limited time with the full swing". Using the GreenGlider, golfers can vastly improve their putting effectiveness with significantly less time and effort than other practice methods. Our company mantra, "precision practice" is the "how" in our solution, but ROPI - Return on Parctice Investment - is our real value proposition.
Target Market(s)
Golfers age 18 to 75 with low-medium to high disposable income
Industry/Entity Type
Sports and Leisure

```html
<!DOCTYPE html>
<html lang="en">
<head>
<meta charset="utf-8">
<title>GreenGlider – Presentation Template Overview</title>
<link rel="stylesheet" href="https://fonts.googleapis.com/css2?family=Montserrat:wght@300;400;500;600;700&display=swap">
<style>
:root{
  --red:#d71920;
  --red-soft:#f04a4f;
  --black:#161616;
  --ink:#222;
  --grey:#8a8a8a;
  --light:#f1f1f1;
  --board:#b4b4b4;
  --white:#fff;
  --navy:#2c3548;
  --turf-a:#5f7e2c;
  --turf-b:#a9c24a;
  --turf-dark:#2f3d1c;
}
*{margin:0;padding:0;box-sizing:border-box}
html,body{width:1200px;height:886px;overflow:hidden}
body{background:var(--board);font-family:'Montserrat',sans-serif;color:var(--ink);position:relative}
.slide{position:absolute;width:254px;height:143px;background:var(--white);overflow:hidden;box-shadow:0 2px 5px rgba(0,0,0,.18)}
.slide.tint{background:var(--light)}
.side{position:absolute;left:0;top:0;width:10px;height:100%;background:var(--red);z-index:5}
.side .menu{position:absolute;top:0;left:0;width:10px;height:10px;background:#2a2a2a}
.side .menu i{position:absolute;left:3px;width:4px;height:.6px;background:#bbb}
.side .brand{position:absolute;bottom:0;left:0;width:10px;height:33px;background:var(--black)}
.side .brand span{position:absolute;left:5px;bottom:12px;transform-origin:0 0;transform:rotate(-90deg) translateY(-50%);font-size:2.6px;font-weight:700;color:#fff;white-space:nowrap;letter-spacing:.2px}
.side .brand b{position:absolute;left:2.5px;bottom:4px;width:5px;height:5px;border-radius:50%;border:1px solid var(--red)}
.foot{position:absolute;left:19px;bottom:8px;font-size:2.8px;color:#aaa;letter-spacing:.6px;z-index:4}
.foot b{color:var(--ink);font-weight:700}
.pg{position:absolute;right:6px;bottom:8px;font-size:2.6px;color:#bbb;z-index:4}
.abs{position:absolute}
.photo{position:absolute;background:linear-gradient(160deg,var(--turf-b),var(--turf-a) 55%,var(--turf-dark))}
.photo.dark{background:linear-gradient(160deg,#4a5a3a,#26301c 60%,#111)}
.photo.sky{background:linear-gradient(180deg,#9cc1df,#cfdde3 45%,#6d8b3a 75%,#3f5a22)}
.photo.warm{background:linear-gradient(150deg,#c9a25e,#7e8f3a 50%,#2e3a18)}
.photo.mono{background:linear-gradient(160deg,#d8d8d8,#7a7a7a 60%,#2e2e2e)}
.photo.rust{background:linear-gradient(140deg,#c9856b,#8a3b2a 55%,#4a1a12)}
.photo.map{background:linear-gradient(150deg,#efe9dc,#e2d6c0 50%,#d9c7b3)}
.sub{font-size:2.9px;letter-spacing:.8px;color:var(--red-soft);font-weight:400}
.sub.dk{color:#555}
.h{font-weight:600;font-size:6.4px;color:var(--ink);line-height:1.15}
.h.c{text-align:center}
.big{font-size:9.5px;font-weight:600;line-height:1.1;color:var(--ink)}
.big span,.lt{font-weight:300}
.txt{font-size:2.7px;line-height:1.45;color:#666}
.txt.w{color:#ddd}
.red{color:var(--red)}
.w{color:#fff}
.btn{position:absolute;background:var(--black);color:#fff;font-size:2.6px;border-radius:4px;padding:1.6px 7px}
.circle{position:absolute;border-radius:50%}
.card{position:absolute;background:#fff;border-radius:2px;box-shadow:0 1px 3px rgba(0,0,0,.12)}
.tag{position:absolute;background:var(--red);color:#fff;font-size:3.2px;padding:1.5px 0;text-align:center}
</style>
</head>
<body>

<!-- 1 Cover -->
<section class="slide" style="left:45px;top:46px">
  <div class="side"><div class="menu"><i style="top:3px"></i><i style="top:5px"></i><i style="top:7px"></i></div><div class="brand"><span>GreenGlider</span><b></b></div></div>
  <div class="photo" role="img" aria-label="Gloved hand placing a golf ball beside a putter on the green" style="left:10px;top:0;width:244px;height:143px"></div>
  <div class="abs" style="left:21px;top:85px;font-size:7.5px;font-weight:600;color:#fff;letter-spacing:.2px">GreenGlider</div>
  <div class="abs" style="left:21px;top:97px;font-size:4px;color:#e6e6e6">Simple, precision practice</div>
  <div class="abs" style="left:19px;top:110px;width:80px;height:10px;background:var(--red);color:#fff;font-size:3.3px;text-align:center;line-height:10px">Presented by <b>Sam Carter</b></div>
</section>

<!-- 2 Precision -->
<section class="slide" style="left:330px;top:46px">
  <div class="side"><div class="menu"><i style="top:3px"></i><i style="top:5px"></i><i style="top:7px"></i></div><div class="brand"><span>GreenGlider</span><b></b></div></div>
  <div class="abs sub dk" style="left:20px;top:31px">Enter your best sub title</div>
  <div class="abs big" style="left:20px;top:41px">Precision <span>in</span><br><span>everyday</span></div>
  <div class="abs txt" style="left:20px;top:69px;width:70px">Lorem ipsum has been the industry's standard dummy text ever since the 1500s, when an unknown printer took a galley of type and scrambled it to make a type specimen book.</div>
  <div class="photo dark" role="img" aria-label="Hand placing a golf ball on a tee beside a driver" style="left:131px;top:22px;width:123px;height:100px;border-radius:50px 0 0 50px"></div>
  <div class="circle" style="left:103px;top:48px;width:40px;height:40px;background:rgba(215,25,32,.15)"></div>
  <div class="circle" style="left:108px;top:53px;width:30px;height:30px;background:rgba(215,25,32,.3)"></div>
  <div class="circle" style="left:112px;top:57px;width:22px;height:22px;background:var(--red);color:#fff;font-size:4px;text-align:center;line-height:22px">2022</div>
  <div class="foot"><b>2022</b> All right Reserved</div><div class="pg">2</div>
</section>

<!-- 3 Stats card -->
<section class="slide tint" style="left:616px;top:46px">
  <div class="side"><div class="menu"><i style="top:3px"></i><i style="top:5px"></i><i style="top:7px"></i></div><div class="brand"><span>GreenGlider</span><b></b></div></div>
  <div class="photo warm" role="img" aria-label="Putter head behind a golf ball on sunlit grass" style="left:20px;top:14px;width:148px;height:114px"></div>
  <div class="abs" style="left:20px;top:29px;width:86px;height:52px;background:#fff;padding:10px 9px">
    <div class="h" style="font-size:5.5px">Enter your best<br>title here</div>
    <div class="txt" style="margin-top:4px">It has survived not only five centuries, but also the leap into electronic typesetting, remaining essentially unchanged.</div>
  </div>
  <div class="abs" style="left:118px;top:82px;width:46px;height:44px;background:rgba(255,255,255,.55)"></div>
  <svg class="abs" style="left:128px;top:83px" width="24" height="24" viewBox="0 0 24 24"><circle cx="12" cy="12" r="10" fill="none" stroke="#ddd" stroke-width="1.2"/><path d="M12 2 A10 10 0 0 1 21.5 15" fill="none" stroke="#d71920" stroke-width="1.2"/><text x="12" y="14" text-anchor="middle" font-size="6" font-family="Montserrat" font-weight="600" fill="#222">30%</text></svg>
  <div class="abs txt" style="left:121px;top:109px;width:42px;text-align:center">Lorem ipsum is not simply random text.</div>
  <div class="abs" style="left:168px;top:14px;width:66px;height:114px;background:#fff;padding:8px 9px">
    <div style="font-size:12px;font-weight:600">25<sup style="font-size:6px;font-weight:300">%</sup></div>
    <div class="red" style="font-size:4.5px;font-weight:500;line-height:1.1">Enter your<br><b>best title here</b></div>
    <div class="txt" style="margin-top:2px">Lorem Ipsum is simply dummy text of the printing and typesetting industry.</div>
    <div style="font-size:12px;font-weight:600;margin-top:5px">60<sup style="font-size:6px;font-weight:300">%</sup></div>
    <div class="red" style="font-size:4.5px;font-weight:500;line-height:1.1">Enter your<br><b>best title here</b></div>
    <div class="txt" style="margin-top:2px">Lorem Ipsum is simply dummy text of the printing and typesetting industry.</div>
  </div>
  <div class="foot"><b>2022</b> All right Reserved</div><div class="pg">3</div>
</section>

<!-- 4 Three features -->
<section class="slide" style="left:901px;top:46px">
  <div class="side"><div class="menu"><i style="top:3px"></i><i style="top:5px"></i><i style="top:7px"></i></div><div class="brand"><span>GreenGlider</span><b></b></div></div>
  <div class="photo sky" role="img" aria-label="Coach helping a golfer with a stance beside a golf bag on the course" style="left:12px;top:0;width:242px;height:86px"></div>
  <svg class="abs" style="left:52px;top:0" width="200" height="32" viewBox="0 0 200 32"><polygon points="0,0 200,0 128,0 200,0" fill="#111"/><polygon points="2,0 198,0 100,31" fill="#111"/></svg>
  <div class="abs w" style="left:90px;top:5px;width:80px;text-align:center;font-size:4.2px;font-weight:600">Best title here</div>
  <div class="abs txt w" style="left:105px;top:13px;width:50px;text-align:center">Lorem Ipsum is not simply random text</div>
  <div class="circle" style="left:31px;top:73px;width:21px;height:21px;background:var(--red);border:2.5px solid #fff;box-shadow:0 0 0 1px rgba(0,0,0,.1)"></div>
  <div class="circle" style="left:112px;top:73px;width:21px;height:21px;background:var(--red);border:2.5px solid #fff;box-shadow:0 0 0 1px rgba(0,0,0,.1)"></div>
  <div class="circle" style="left:194px;top:73px;width:21px;height:21px;background:var(--red);border:2.5px solid #fff;box-shadow:0 0 0 1px rgba(0,0,0,.1)"></div>
  <svg class="abs" style="left:36px;top:78px" width="176" height="11" viewBox="0 0 176 11" fill="none" stroke="#fff" stroke-width=".8"><path d="M5 1v8M5 1l4 2-4 2M2 10h7"/><circle cx="86" cy="4" r="3"/><path d="M86 7v4"/><path d="M167 1v9M167 1h6v4h-6"/></svg>
  <div class="abs" style="left:12px;top:98px;width:242px;display:flex;justify-content:space-around;text-align:center">
    <div style="width:60px"><div class="h" style="font-size:4.2px">Enter your best<br>title here</div><div class="txt" style="margin-top:2px">Lorem Ipsum is simply dummy text of the printing and typesetting industry.</div></div>
    <div style="width:60px"><div class="h" style="font-size:4.2px">Enter your best<br>title here</div><div class="txt" style="margin-top:2px">Lorem Ipsum is simply dummy text of the printing and typesetting industry.</div></div>
    <div style="width:60px"><div class="h" style="font-size:4.2px">Enter your best<br>title here</div><div class="txt" style="margin-top:2px">Lorem Ipsum is simply dummy text of the printing and typesetting industry.</div></div>
  </div>
  <div class="foot"><b>2022</b> All right Reserved</div><div class="pg">4</div>
</section>

<!-- 5 Hole records -->
<section class="slide tint" style="left:45px;top:209px">
  <div class="side"><div class="menu"><i style="top:3px"></i><i style="top:5px"></i><i style="top:7px"></i></div><div class="brand"><span>GreenGlider</span><b></b></div></div>
  <div class="abs h" style="left:19px;top:17px">Enter your best title here</div>
  <div class="abs txt" style="left:19px;top:28px;width:125px"><b style="color:#222">Contrary to popular belief,</b> Lorem Ipsum is not simply random text. It has roots in a piece of classical Latin literature, making it over 2000 years old.</div>
  <div class="photo sky" role="img" aria-label="Golfer swinging with three balls in the foreground" style="left:19px;top:48px;width:55px;height:71px"></div>
  <div class="photo sky" role="img" aria-label="Golfer putting toward the flag in front of mountains" style="left:90px;top:48px;width:55px;height:71px"></div>
  <svg class="abs" style="left:64px;top:109px" width="10" height="10"><polygon points="10,0 10,10 0,10" fill="#d71920"/></svg>
  <svg class="abs" style="left:135px;top:109px" width="10" height="10"><polygon points="10,0 10,10 0,10" fill="#d71920"/></svg>
  <div class="abs" style="left:160px;top:0;width:80px;height:119px;background:var(--black);padding:20px 8px">
    <div class="sub">Your best sub title</div>
    <div class="w" style="font-size:8px;font-weight:600;line-height:1.15;margin-top:2px">Hole Records<br><span class="lt">of This Season</span></div>
    <div class="txt w" style="margin-top:7px;color:#aaa">Lorem Ipsum has been the industry's standard dummy text ever since the 1500s, when an unknown printer took a galley of type and scrambled it to make a type specimen book.</div>
    <div class="abs" style="left:8px;top:92px;border:.6px solid #ccc;border-radius:5px;color:#ddd;font-size:3px;padding:2px 9px">Learn More</div>
  </div>
  <div class="foot"><b>2022</b> All right Reserved</div><div class="pg">5</div>
</section>

<!-- 6 Stats + image -->
<section class="slide" style="left:330px;top:209px">
  <div class="side"><div class="menu"><i style="top:3px"></i><i style="top:5px"></i><i style="top:7px"></i></div><div class="brand"><span>GreenGlider</span><b></b></div></div>
  <svg class="abs" style="left:19px;top:25px" width="14" height="14" fill="none" stroke="#555" stroke-width=".7"><path d="M6 1v11M6 1l5 2.5L6 6M1 12.5h12"/></svg>
  <div class="abs" style="left:38px;top:22px"><div style="font-size:13px;font-weight:600">25<sup style="font-size:6px;font-weight:300">%</sup></div><div class="red" style="font-size:4.6px;font-weight:500;line-height:1.1">Enter your<br><b>best title here</b></div><div class="txt" style="width:56px;margin-top:2px">Lorem Ipsum is simply dummy text of the printing and typesetting industry.</div></div>
  <svg class="abs" style="left:19px;top:78px" width="14" height="14" fill="none" stroke="#555" stroke-width=".7"><path d="M2 2c4 0 6 3 7 7M8 9l4 3M4 12h8"/></svg>
  <div class="abs" style="left:38px;top:75px"><div style="font-size:13px;font-weight:600">60<sup style="font-size:6px;font-weight:300">%</sup></div><div class="red" style="font-size:4.6px;font-weight:500;line-height:1.1">Enter your<br><b>best title here</b></div><div class="txt" style="width:56px;margin-top:2px">Lorem Ipsum is simply dummy text of the printing and typesetting industry.</div></div>
  <div class="photo" role="img" aria-label="Close-up of a golf ball in long grass" style="left:102px;top:0;width:152px;height:143px;clip-path:polygon(30% 0,100% 0,100% 100%,0 100%)"></div>
  <div class="abs" style="left:110px;top:50px;width:116px;height:52px;background:rgba(10,10,10,.85);clip-path:polygon(10% 0,100% 0,90% 100%,0 100%)"></div>
  <div class="abs" style="left:217px;top:50px;width:10px;height:52px;background:var(--red);clip-path:polygon(60% 0,100% 0,40% 100%,0 100%)"></div>
  <div class="abs sub" style="left:133px;top:59px">Your best sub title</div>
  <div class="abs w" style="left:133px;top:65px;font-size:9.5px;font-weight:600;line-height:1.15">Precision <span class="lt">in</span><br><span class="lt">everyday</span></div>
  <div class="foot"><b>2022</b> All right Reserved</div><div class="pg" style="color:#eee">6</div>
</section>

<!-- 7 Annual report -->
<section class="slide" style="left:616px;top:209px">
  <div class="side"><div class="menu"><i style="top:3px"></i><i style="top:5px"></i><i style="top:7px"></i></div><div class="brand"><span>GreenGlider</span><b></b></div></div>
  <div class="abs sub" style="left:19px;top:11px">Your best sub title</div>
  <div class="abs h" style="left:19px;top:17px">Annual Report</div>
  <svg class="abs" style="left:18px;top:31px" width="44" height="20" fill="none" stroke="#222" stroke-width=".8"><circle cx="10" cy="10" r="9"/><circle cx="31" cy="10" r="9"/><path d="M6 14l8-8M7 6l7 8M31 5v10M29 5h4"/></svg>
  <div class="abs" style="left:76px;top:31px;font-size:4.4px;font-weight:500">Company budget files 2021</div>
  <div class="abs txt" style="left:76px;top:38px;width:118px;font-size:2.3px;font-style:italic">Lorem ipsum dolor sit amet, ligula suspendisse nulla pretium, rhoncus tempor fermentum, enim integer ad vestibulum volutpat. Nisl rhoncus turpis est, vel elit, congue wisi enim nunc.</div>
  <table class="abs" style="left:17px;top:57px;width:178px;border-collapse:collapse;font-size:2.9px;color:#777">
    <tr style="color:var(--red);font-size:3.4px"><td style="padding:1.2px 2px">Nisl rhoncus turpis est</td><td>2014</td><td>2015</td><td>2016</td><td>2017</td></tr>
    <tr style="border-top:.4px solid #ddd"><td style="padding:1.8px 2px">Praesent condimentum arcu</td><td>4.456</td><td>4.456</td><td>4.456</td><td>4.456</td></tr>
    <tr style="border-top:.4px solid #ddd"><td style="padding:1.8px 2px">Praesent condimentum arcu</td><td>5.345</td><td>5.345</td><td>5.345</td><td>5.345</td></tr>
    <tr style="border-top:.4px solid #ddd"><td style="padding:1.8px 2px">Praesent condimentum arcu</td><td>6.567</td><td>6.567</td><td>6.567</td><td>6.567</td></tr>
    <tr style="border-top:.4px solid #ddd"><td style="padding:1.8px 2px">Praesent condimentum arcu</td><td>7.678</td><td>7.678</td><td>7.678</td><td>7.678</td></tr>
    <tr style="border-top:.4px solid #ddd"><td style="padding:1.8px 2px">Praesent condimentum arcu</td><td>8.789</td><td>8.789</td><td>8.789</td><td>8.789</td></tr>
    <tr style="border-top:.4px solid #ddd;border-bottom:.6px solid #222;color:#222;font-weight:600"><td style="padding:1.5px 2px">CHANGE 20%</td><td></td><td></td><td></td><td></td></tr>
  </table>
  <div class="abs" style="left:199px;top:30px;width:55px;height:97px;background:var(--red-soft)">
    <div style="background:#444;color:#fff;font-size:3.3px;padding:3px 6px">STATS MANAGER</div>
    <div style="padding:4px 6px;font-size:3.3px;color:#fff;line-height:1.3">
      <div style="border-bottom:.5px solid rgba(255,255,255,.4);padding-bottom:4px">THIS YEAR<br>17,250</div>
      <div style="border-bottom:.5px solid rgba(255,255,255,.4);padding:4px 0">THIS MONTH<br>3,000</div>
      <div style="border-bottom:.5px solid rgba(255,255,255,.4);padding:4px 0">THIS WEEK<br>450</div>
      <div style="padding-top:4px">TODAY<br>225</div>
    </div>
  </div>
  <div class="foot"><b>2022</b> All right Reserved</div><div class="pg">7</div>
</section>

<!-- 8 Overview chart -->
<section class="slide" style="left:901px;top:209px">
  <div class="side"><div class="menu"><i style="top:3px"></i><i style="top:5px"></i><i style="top:7px"></i></div><div class="brand"><span>GreenGlider</span><b></b></div></div>
  <div class="abs sub" style="left:0;width:254px;text-align:center;top:11px">Your best sub title</div>
  <div class="abs h c" style="left:0;width:254px;top:17px">Overview Chart</div>
  <div class="abs" style="left:0;width:254px;top:31px;text-align:center;font-size:3.6px;color:#999">Statistic</div>
  <svg class="abs" style="left:0;top:0" width="254" height="143" viewBox="0 0 254 143" font-family="Montserrat" font-size="2.6" fill="#999">
    <g stroke="#ececec" stroke-width=".4"><line x1="25" y1="40" x2="230" y2="40"/><line x1="25" y1="55" x2="230" y2="55"/><line x1="25" y1="70" x2="230" y2="70"/><line x1="25" y1="85" x2="230" y2="85"/><line x1="25" y1="100" x2="230" y2="100"/><line x1="25" y1="115" x2="230" y2="115"/></g>
    <text x="18" y="41">5</text><text x="18" y="56">4</text><text x="18" y="71">3</text><text x="18" y="86">2</text><text x="18" y="101">1</text><text x="18" y="116">0</text>
    <text x="57" y="121">may</text><text x="103" y="121">jun</text><text x="149" y="121">jul</text><text x="194" y="121">aug</text>
    <path d="M62 50 C80 60,90 83,107 84 S135 73,153 62 S185 50,198 47" fill="none" stroke="#333" stroke-width=".8"/>
    <path d="M62 79 C80 72,92 52,107 52 S135 90,153 88 S185 80,198 73" fill="none" stroke="#d71920" stroke-width=".8"/>
    <g fill="#fff" stroke-width=".8"><circle cx="62" cy="50" r="1.6" stroke="#333"/><circle cx="107" cy="84" r="1.6" stroke="#333"/><circle cx="153" cy="62" r="1.6" stroke="#333"/><circle cx="198" cy="47" r="1.6" stroke="#333"/><circle cx="62" cy="79" r="1.6" stroke="#d71920"/><circle cx="107" cy="52" r="1.6" stroke="#d71920"/><circle cx="153" cy="88" r="1.6" stroke="#d71920"/><circle cx="198" cy="73" r="1.6" stroke="#d71920"/></g>
    <rect x="98" y="84" width="46" height="26" rx="2" fill="#1e1e1e"/>
    <text x="102" y="90" fill="#f04a4f" font-size="2.4">Enter your best title here</text>
    <text x="102" y="95" fill="#ddd" font-size="2.3">Lorem Ipsum is simply</text>
    <text x="102" y="99" fill="#ddd" font-size="2.3">dummy text of the printing</text>
    <text x="102" y="103" fill="#ddd" font-size="2.3">and typesetting industry.</text>
  </svg>
  <div class="foot"><b>2022</b> All right Reserved</div><div class="pg">8</div>
</section>

<!-- 9 Graph chart -->
<section class="slide" style="left:45px;top:373px">
  <div class="side"><div class="menu"><i style="top:3px"></i><i style="top:5px"></i><i style="top:7px"></i></div><div class="brand"><span>GreenGlider</span><b></b></div></div>
  <div class="abs sub" style="left:0;width:254px;text-align:center;top:11px">Your best sub title</div>
  <div class="abs h c" style="left:0;width:254px;top:17px">Graph Chart</div>
  <svg class="abs" style="left:0;top:0" width="254" height="143" viewBox="0 0 254 143" font-family="Montserrat" font-size="3" fill="#888">
    <g stroke="#ececec" stroke-width=".4"><line x1="27" y1="40" x2="150" y2="40"/><line x1="27" y1="52" x2="150" y2="52"/><line x1="27" y1="64" x2="150" y2="64"/><line x1="27" y1="76" x2="150" y2="76"/><line x1="27" y1="88" x2="150" y2="88"/><line x1="27" y1="100" x2="150" y2="100"/></g>
    <line x1="27" y1="112" x2="150" y2="112" stroke="#333" stroke-width=".5"/>
    <text x="20" y="41">6</text><text x="20" y="53">5</text><text x="20" y="65">4</text><text x="20" y="77">3</text><text x="20" y="89">2</text><text x="20" y="101">1</text><text x="20" y="113">0</text>
    <rect x="36" y="60.4" width="7" height="51.6" fill="#111"/><rect x="44" y="82" width="7" height="30" fill="#888"/><rect x="52" y="58" width="7" height="54" fill="#d71920"/>
    <rect x="77" y="52" width="7" height="60" fill="#111"/><rect x="85" y="70" width="7" height="42" fill="#888"/><rect x="93" y="76" width="7" height="36" fill="#d71920"/>
    <rect x="118" y="83.2" width="7" height="28.8" fill="#111"/><rect x="126" y="59.2" width="7" height="52.8" fill="#888"/><rect x="134" y="78.4" width="7" height="33.6" fill="#d71920"/>
    <text x="37" y="119">category 1</text><text x="78" y="119">category 2</text><text x="119" y="119">category 3</text>
    <circle cx="164" cy="41" r="6" fill="#111"/><circle cx="164" cy="69" r="6" fill="#888"/><circle cx="164" cy="97" r="6" fill="#d71920"/>
    <g stroke="#fff" stroke-width=".6" fill="none"><rect x="161.5" y="39" width="5" height="4"/><rect x="161.5" y="67" width="5" height="4"/><rect x="161.5" y="95" width="5" height="4"/></g>
  </svg>
  <div class="abs" style="left:176px;top:37px"><div style="font-size:4.2px;font-weight:500">option one</div><div class="txt" style="width:52px;color:#aaa">Lorem ipsum dolor sit amet, consectetuer adipiscing elit.</div></div>
  <div class="abs" style="left:176px;top:65px"><div style="font-size:4.2px;font-weight:500">option two</div><div class="txt" style="width:52px;color:#aaa">Lorem ipsum dolor sit amet, consectetuer adipiscing elit.</div></div>
  <div class="abs" style="left:176px;top:93px"><div style="font-size:4.2px;font-weight:500">option three</div><div class="txt" style="width:52px;color:#aaa">Lorem ipsum dolor sit amet, consectetuer adipiscing elit.</div></div>
  <div class="foot"><b>2022</b> All right Reserved</div><div class="pg">9</div>
</section>

<!-- 10 Number infographic -->
<section class="slide tint" style="left:330px;top:373px">
  <div class="side"><div class="menu"><i style="top:3px"></i><i style="top:5px"></i><i style="top:7px"></i></div><div class="brand"><span>GreenGlider</span><b></b></div></div>
  <div class="abs sub" style="left:0;width:254px;text-align:center;top:11px">Your best sub title</div>
  <div class="abs h c" style="left:0;width:254px;top:17px">Number Infographic</div>
  <div class="abs" style="left:47px;top:30px;width:55px"><div class="red" style="font-size:3.6px;font-weight:500;line-height:1.1">Enter your best<br>title here</div><div class="txt">Lorem Ipsum is simply dummy text of the printing and typesetting industry.</div></div>
  <div class="abs" style="left:140px;top:30px;width:55px"><div class="red" style="font-size:3.6px;font-weight:500;line-height:1.1">Enter your best<br>title here</div><div class="txt">Lorem Ipsum is simply dummy text of the printing and typesetting industry.</div></div>
  <div class="abs" style="left:47px;top:108px;width:68px;text-align:right"><div class="red" style="font-size:3.6px;font-weight:500;line-height:1.1">Enter your best<br>title here</div><div class="txt">Lorem Ipsum is simply dummy text of the printing and typesetting industry.</div></div>
  <div class="abs" style="left:140px;top:108px;width:68px;text-align:right"><div class="red" style="font-size:3.6px;font-weight:500;line-height:1.1">Enter your best<br>title here</div><div class="txt">Lorem Ipsum is simply dummy text of the printing and typesetting industry.</div></div>
  <svg class="abs" style="left:0;top:0" width="254" height="143" viewBox="0 0 254 143" font-family="Montserrat">
    <g fill="#fff" stroke="#e3e3e3" stroke-width=".5"><circle cx="59" cy="82" r="22"/><circle cx="104" cy="82" r="22"/><circle cx="150" cy="82" r="22"/><circle cx="196" cy="82" r="22"/></g>
    <g fill="none" stroke="#d71920" stroke-width=".8"><path d="M40 93 A22 22 0 0 0 78 93"/><path d="M85 71 A22 22 0 0 1 123 71"/><path d="M131 93 A22 22 0 0 0 169 93"/><path d="M177 71 A22 22 0 0 1 215 71"/></g>
    <g fill="#d71920" stroke="#fff" stroke-width=".8"><circle cx="59" cy="104" r="3.6"/><circle cx="104" cy="60" r="3.6"/><circle cx="150" cy="104" r="3.6"/><circle cx="196" cy="60" r="3.6"/></g>
    <g font-size="11" font-weight="500" text-anchor="middle" fill="#222"><text x="59" y="86">205</text><text x="104" y="86">48</text><text x="150" y="86">100</text><text x="196" y="86">25</text></g>
  </svg>
  <div class="foot"><b>2022</b> All right Reserved</div><div class="pg">10</div>
</section>

<!-- 11 Timeline -->
<section class="slide" style="left:616px;top:373px">
  <div class="side"><div class="menu"><i style="top:3px"></i><i style="top:5px"></i><i style="top:7px"></i></div><div class="brand"><span>GreenGlider</span><b></b></div></div>
  <div class="abs sub" style="left:0;width:254px;text-align:center;top:11px">Your best sub title</div>
  <div class="abs h c" style="left:0;width:254px;top:17px">Our Timeline</div>
  <svg class="abs" style="left:0;top:0" width="254" height="143" viewBox="0 0 254 143" font-family="Montserrat">
    <polygon points="0,44 85,44 83,49 0,49" fill="#888"/><polygon points="85,44 230,44 226,49 83,49" fill="#d71920"/>
    <g stroke="#9aa" stroke-width=".4"><line x1="81" y1="49" x2="81" y2="74"/><line x1="113" y1="49" x2="113" y2="86"/><line x1="157" y1="49" x2="157" y2="62"/><line x1="227" y1="49" x2="227" y2="103"/></g>
    <g fill="#111"><circle cx="81" cy="76" r="6"/><circle cx="113" cy="92" r="6"/><circle cx="157" cy="69" r="6"/><circle cx="227" cy="110" r="6"/></g>
    <g fill="#fff" font-size="2.8" text-anchor="middle"><text x="81" y="80">2015</text><text x="113" y="96">2017</text><text x="157" y="73">2020</text><text x="227" y="114">2022</text></g>
    <g fill="#d71920"><circle cx="81" cy="73" r="1.3"/><circle cx="113" cy="89" r="1.3"/><circle cx="157" cy="66" r="1.3"/><circle cx="227" cy="107" r="1.3"/></g>
  </svg>
  <div class="abs" style="left:22px;top:67px;width:50px;text-align:center"><div style="font-size:3.6px;font-weight:600">Your subtitle here</div><div class="txt">Lorem Ipsum is simply dummy text of the printing and typesetting industry.</div></div>
  <div class="abs" style="left:127px;top:86px;width:45px"><div style="font-size:3.6px;font-weight:600">Your subtitle here</div><div class="txt">Lorem Ipsum is simply dummy text of the printing and typesetting industry.</div></div>
  <div class="abs" style="left:170px;top:61px;width:45px"><div style="font-size:3.6px;font-weight:600">Your subtitle here</div><div class="txt">Lorem Ipsum is simply dummy text of the printing and typesetting industry.</div></div>
  <div class="abs" style="left:170px;top:108px;width:48px;text-align:right"><div style="font-size:3.6px;font-weight:600">Your subtitle here</div><div class="txt">Lorem Ipsum is simply dummy text of the printing and typesetting industry.</div></div>
  <div class="foot"><b>2022</b> All right Reserved</div><div class="pg">11</div>
</section>

<!-- 12 Milestone -->
<section class="slide" style="left:901px;top:373px">
  <div class="side"><div class="menu"><i style="top:3px"></i><i style="top:5px"></i><i style="top:7px"></i></div><div class="brand"><span>GreenGlider</span><b></b></div></div>
  <div class="abs sub" style="left:0;width:254px;text-align:center;top:11px">Your best sub title</div>
  <div class="abs h c" style="left:0;width:254px;top:17px">Our Milestone</div>
  <svg class="abs" style="left:0;top:0" width="254" height="143" viewBox="0 0 254 143" font-family="Montserrat">
    <line x1="14" y1="116" x2="237" y2="116" stroke="#222" stroke-width=".4" stroke-dasharray="1 1"/>
    <g stroke-width="1.2"><line x1="48" y1="76" x2="48" y2="116" stroke="#555"/><line x1="86" y1="58" x2="86" y2="116" stroke="#333"/><line x1="123" y1="76" x2="123" y2="116" stroke="#222"/><line x1="161" y1="58" x2="161" y2="116" stroke="#111"/><line x1="198" y1="76" x2="198" y2="116" stroke="#d71920"/></g>
    <circle cx="48" cy="76" r="9" fill="#555"/><circle cx="86" cy="57" r="9" fill="#333"/><circle cx="123" cy="76" r="9" fill="#222"/><circle cx="161" cy="57" r="9" fill="#111"/><circle cx="198" cy="76" r="9" fill="#d71920"/>
    <g fill="#fff" font-size="3.3" text-anchor="middle" font-weight="600"><text x="48" y="77.5">2015</text><text x="86" y="58.5">2017</text><text x="123" y="77.5">2019</text><text x="161" y="58.5">2021</text><text x="198" y="77.5">2023</text></g>
    <g fill="#fff" stroke-width="1"><circle cx="48" cy="116" r="2" stroke="#555"/><circle cx="86" cy="116" r="2" stroke="#333"/><circle cx="123" cy="116" r="2" stroke="#222"/><circle cx="161" cy="116" r="2" stroke="#111"/><circle cx="198" cy="116" r="2" stroke="#d71920"/></g>
    <g fill="#666" font-size="3.2"><text x="53" y="97">Write your</text><text x="53" y="101">paragraph</text><text x="53" y="105">here</text><text x="91" y="97">Write your</text><text x="91" y="101">paragraph</text><text x="91" y="105">here</text><text x="128" y="97">Write your</text><text x="128" y="101">paragraph</text><text x="128" y="105">here</text><text x="166" y="97">Write your</text><text x="166" y="101">paragraph</text><text x="166" y="105">here</text><text x="203" y="97">Write your</text><text x="203" y="101">paragraph</text><text x="203" y="105">here</text></g>
  </svg>
  <div class="foot"><b>2022</b> All right Reserved</div><div class="pg">12</div>
</section>

<!-- 13 World maps -->
<section class="slide" style="left:45px;top:534px">
  <div class="side"><div class="menu"><i style="top:3px"></i><i style="top:5px"></i><i style="top:7px"></i></div><div class="brand"><span>GreenGlider</span><b></b></div></div>
  <div class="abs sub" style="left:0;width:254px;text-align:center;top:11px">Your best sub title</div>
  <div class="abs h c" style="left:0;width:254px;top:17px">World Maps</div>
  <div class="abs" role="img" aria-label="Grey world map with the United States highlighted in red and China in black" style="left:23px;top:43px;width:138px;height:73px;background:radial-gradient(ellipse at 50% 50%,#cfcfcf,#e4e4e4 70%,#fff 100%);border-radius:30%"></div>
  <svg class="abs" style="left:196px;top:33px" width="14" height="12" fill="none" stroke="#d71920" stroke-width=".8"><path d="M3 10h9M7 10V2c-2 1-4 3-5 5M7 2c2 1 4 3 5 5"/></svg>
  <div class="abs" style="left:175px;top:49px;width:56px;text-align:center"><div style="font-size:5px;font-weight:500">we are <span class="red">growing</span></div><div class="txt">Lorem ipsum dolor sit amet, consectetuer adipiscing elit. maecenas</div></div>
  <svg class="abs" style="left:196px;top:76px" width="14" height="12" fill="none" stroke="#222" stroke-width=".8"><path d="M2 3h8c2 0 2-2 0-2M2 6h10c2 0 2 3 0 3M2 9h6"/></svg>
  <div class="abs" style="left:175px;top:92px;width:56px;text-align:center"><div style="font-size:5px;font-weight:500">join the crew</div><div class="txt">Lorem ipsum dolor sit amet, consectetuer adipiscing elit. maecenas</div></div>
</section>

<!-- 14 USA maps -->
<section class="slide" style="left:330px;top:534px">
  <div class="side"><div class="menu"><i style="top:3px"></i><i style="top:5px"></i><i style="top:7px"></i></div><div class="brand"><span>GreenGlider</span><b></b></div></div>
  <div class="abs sub" style="left:0;width:254px;text-align:center;top:11px">Your best sub title</div>
  <div class="abs h c" style="left:0;width:254px;top:17px">USA Maps</div>
  <div class="abs" style="left:21px;top:43px;width:75px;font-size:3.8px;line-height:1.3">Ut wisi enim ad minim veniam, quis nostrud exerci</div>
  <div class="abs txt" style="left:21px;top:55px;width:77px"><b style="color:#222">Ut wisi enim</b> ad minim veniam, quis nostrud exerci tation ullamcorper nibh euismod tincidunt ut laoreet dolore magna aliquam erat volutpat. Ut wisi enim ad minim veniam, quis nostrud exerci tation ullamcorper nibh euismod tincidunt ut laoreet</div>
  <div class="btn" style="left:21px;top:104px">Read More</div>
  <div class="abs" role="img" aria-label="Grey map of the United States with location pins" style="left:125px;top:37px;width:110px;height:72px;background:radial-gradient(ellipse at 50% 50%,#c9c9c9,#dedede 70%,#fff 100%);border-radius:25%"></div>
  <svg class="abs" style="left:125px;top:37px" width="110" height="72" fill="#222"><path d="M14 24a2.2 2.2 0 1 1 4.4 0c0 2-2.2 4-2.2 4s-2.2-2-2.2-4z"/><path d="M34 42a2.2 2.2 0 1 1 4.4 0c0 2-2.2 4-2.2 4s-2.2-2-2.2-4z"/><path d="M86 49a2.2 2.2 0 1 1 4.4 0c0 2-2.2 4-2.2 4s-2.2-2-2.2-4z"/><path d="M46 17a2.2 2.2 0 1 1 4.4 0c0 2-2.2 4-2.2 4s-2.2-2-2.2-4z" fill="#d71920"/></svg>
  <div class="abs" style="left:166px;top:30px;width:70px;height:12px;background:var(--red);color:#fff;padding:2px 3px;display:flex;gap:3px;align-items:center"><b style="font-size:4.5px">70%</b><span style="font-size:2.2px;line-height:1.2">Ut wisi enim ad minim veniam, quis nostrud exerci tation</span></div>
</section>

<!-- 15 Features grid -->
<section class="slide tint" style="left:616px;top:534px">
  <div class="side"><div class="menu"><i style="top:3px"></i><i style="top:5px"></i><i style="top:7px"></i></div><div class="brand"><span>GreenGlider</span><b></b></div></div>
  <div class="photo dark" role="img" aria-label="Golfer lining up a putt on a mountain course" style="left:24px;top:20px;width:79px;height:103px"></div>
  <svg class="abs" style="left:89px;top:109px" width="14" height="14"><polygon points="14,0 14,14 0,14" fill="#111"/></svg>
  <div class="abs w" style="left:30px;top:51px;width:70px;text-align:right;font-size:7px;font-weight:600;line-height:1.15">Precision in<br><span class="red">everyday</span></div>
  <div class="abs txt w" style="left:50px;top:73px;width:50px;text-align:right">Lorem Ipsum is simply dummy text of the printing and typesetting industry.</div>
  <div class="card" style="left:113px;top:20px;width:61px;height:29px"></div><div class="card" style="left:183px;top:20px;width:61px;height:29px"></div>
  <div class="card" style="left:113px;top:56px;width:61px;height:29px"></div><div class="card" style="left:183px;top:56px;width:61px;height:29px"></div>
  <div class="card" style="left:113px;top:92px;width:61px;height:29px"></div><div class="card" style="left:183px;top:92px;width:61px;height:29px"></div>
  <div class="abs" style="left:113px;top:20px;width:131px;display:grid;grid-template-columns:61px 61px;column-gap:9px;row-gap:7px;text-align:center">
    <div style="padding-top:14px"><div style="font-size:3.7px;font-weight:600">we are <span class="red">growing</span></div><div class="txt" style="font-size:2.1px">lorem ipsum dolor sit amet, consectetuer adipiscing elit. maecenas</div></div>
    <div style="padding-top:14px"><div style="font-size:3.7px;font-weight:600">we are <span class="red">growing</span></div><div class="txt" style="font-size:2.1px">lorem ipsum dolor sit amet, consectetuer adipiscing elit. maecenas</div></div>
    <div style="padding-top:14px"><div style="font-size:3.7px;font-weight:600">we are <span class="red">growing</span></div><div class="txt" style="font-size:2.1px">lorem ipsum dolor sit amet, consectetuer adipiscing elit. maecenas</div></div>
    <div style="padding-top:14px"><div style="font-size:3.7px;font-weight:600">we are <span class="red">growing</span></div><div class="txt" style="font-size:2.1px">lorem ipsum dolor sit amet, consectetuer adipiscing elit. maecenas</div></div>
    <div style="padding-top:14px"><div style="font-size:3.7px;font-weight:600">we are <span class="red">growing</span></div><div class="txt" style="font-size:2.1px">lorem ipsum dolor sit amet, consectetuer adipiscing elit. maecenas</div></div>
    <div style="padding-top:14px"><div style="font-size:3.7px;font-weight:600">we are <span class="red">growing</span></div><div class="txt" style="font-size:2.1px">lorem ipsum dolor sit amet, consectetuer adipiscing elit. maecenas</div></div>
  </div>
  <svg class="abs" style="left:113px;top:20px" width="131" height="101" fill="none" stroke="#333" stroke-width=".6"><path d="M29 3v8M29 3l4 2-4 2M25 12h8"/><path d="M96 3l6 8M102 3l-6 8"/><path d="M29 40v8M29 40h5v3h-5"/><path d="M96 40c3 0 5 2 5 6M100 46l2 2"/><circle cx="29" cy="78" r="2"/><path d="M29 80v5M26 85h6"/><circle cx="100" cy="78" r="2.3"/><path d="M100 80v5"/></svg>
  <div class="foot"><b>2022</b> All right Reserved</div><div class="pg">15</div>
</section>

<!-- 16 Precision focus -->
<section class="slide" style="left:901px;top:534px">
  <div class="side"><div class="menu"><i style="top:3px"></i><i style="top:5px"></i><i style="top:7px"></i></div><div class="brand"><span>GreenGlider</span><b></b></div></div>
  <div class="photo dark" role="img" aria-label="Golf ball on a tee against a dark grass background" style="left:10px;top:0;width:244px;height:143px"></div>
  <svg class="abs" style="left:10px;top:95px" width="244" height="48"><path d="M0 10 Q122 40 244 10 V48 H0 Z" fill="#fff"/></svg>
  <div class="abs w" style="left:10px;width:244px;top:5px;text-align:center;font-size:9px;font-weight:600;line-height:1.15">Precision <span style="color:var(--red-soft)">make</span> focus<br>for your life</div>
  <div class="abs txt w" style="left:50px;width:164px;top:28px;text-align:center">Lorem Ipsum has been the industry's standard dummy text ever since the 1500s, when an unknown printer took a galley of type and scrambled it to make a type specimen book.</div>
  <div class="tag" style="left:29px;top:58px;width:50px;clip-path:polygon(0 0,100% 0,100% 60%,92% 100%,0 100%)">Training 1</div>
  <div class="tag" style="left:103px;top:58px;width:50px;clip-path:polygon(0 0,100% 0,100% 60%,92% 100%,0 100%)">Training 1</div>
  <div class="tag" style="left:177px;top:58px;width:50px;clip-path:polygon(0 0,100% 0,100% 60%,92% 100%,0 100%)">Training 1</div>
  <div class="circle" style="left:114px;top:99px;width:25px;height:25px;background:#fff;box-shadow:0 1px 3px rgba(0,0,0,.25)"></div>
  <div class="circle" style="left:117px;top:102px;width:19px;height:19px;background:var(--red);color:#fff;font-size:3.4px;text-align:center;line-height:1.1;padding-top:5px">25<br>Dec</div>
  <div class="foot"><b>2022</b> All right Reserved</div><div class="pg">16</div>
</section>

<!-- 17 Photo grid records -->
<section class="slide" style="left:45px;top:696px">
  <div class="side"><div class="menu"><i style="top:3px"></i><i style="top:5px"></i><i style="top:7px"></i></div><div class="brand"><span>GreenGlider</span><b></b></div></div>
  <div class="photo" role="img" aria-label="Golf ball on a tee with a club behind it" style="left:11px;top:11px;width:166px;height:60px"></div>
  <div class="photo mono" role="img" aria-label="Black and white close-up of a gloved hand gripping a club" style="left:179px;top:11px;width:64px;height:60px"></div>
  <div class="photo mono" role="img" aria-label="Golf ball on a tee in black and white" style="left:112px;top:73px;width:65px;height:60px"></div>
  <div class="photo dark" role="img" aria-label="Hand holding a golf ball at dusk" style="left:179px;top:73px;width:64px;height:60px"></div>
  <div class="abs w" style="left:19px;top:26px;font-size:9.5px;font-weight:600;line-height:1.3">Precision <span class="lt">in</span><br><span class="lt">everyday</span></div>
  <div class="abs" style="left:150px;top:11px;width:27px;height:27px;background:var(--red);color:#fff;text-align:center;padding-top:4px"><div style="font-size:11px;font-weight:600;line-height:1">15</div><div style="font-size:3.3px">09 PM</div></div>
  <div class="abs" style="left:216px;top:11px;width:27px;height:27px;background:var(--red);color:#fff;text-align:center;padding-top:4px"><div style="font-size:11px;font-weight:600;line-height:1">05</div><div style="font-size:3.3px">09 PM</div></div>
  <div class="abs" style="left:150px;top:73px;width:27px;height:27px;background:var(--red);color:#fff;text-align:center;padding-top:4px"><div style="font-size:11px;font-weight:600;line-height:1">03</div><div style="font-size:3.3px">09 PM</div></div>
  <div class="abs" style="left:216px;top:73px;width:27px;height:27px;background:var(--red);color:#fff;text-align:center;padding-top:4px"><div style="font-size:11px;font-weight:600;line-height:1">01</div><div style="font-size:3.3px">09 PM</div></div>
  <div class="abs sub" style="left:19px;top:77px">Your best sub title</div>
  <div class="abs" style="left:19px;top:84px;font-size:7px;font-weight:600;line-height:1.15">Hole Records <span class="lt">of This</span><br><span class="lt">Season</span></div>
  <div class="abs txt" style="left:19px;top:106px;width:88px">Lorem Ipsum has been the industry's standard dummy text ever since the 1500s, when an unknown printer took a galley of type and scrambled it to make a type specimen book.</div>
  <div class="foot"><b>2022</b> All right Reserved</div><div class="pg">17</div>
</section>

<!-- 18 Collage -->
<section class="slide" style="left:330px;top:696px">
  <div class="side"><div class="menu"><i style="top:3px"></i><i style="top:5px"></i><i style="top:7px"></i></div><div class="brand"><span>GreenGlider</span><b></b></div></div>
  <div class="abs sub" style="left:19px;top:11px">Your best sub title</div>
  <div class="abs" style="left:19px;top:18px;font-size:7.5px;font-weight:600;line-height:1.15">Precision <span class="lt">in</span><br><span class="lt">everyday</span></div>
  <div class="abs txt" style="left:19px;top:38px;width:70px"><b style="color:#222">Ut wisi enim</b> ad minim veniam, quis nostrud exerci tation ullamcorper nibh euismod tincidunt ut laoreet dolore magna aliquam erat volutpat. Ut wisi enim ad minim veniam, quis nostrud exerci. exerci tation ullamcorper nibh euismod tincidunt ut laoreet</div>
  <div class="btn" style="left:19px;top:104px">Read More</div>
  <div class="photo sky" role="img" aria-label="Golfer finishing a full swing on a hillside course" style="left:90px;top:0;width:55px;height:143px"></div>
  <div class="photo" role="img" aria-label="Golf ball sitting on bright grass" style="left:145px;top:0;width:55px;height:79px"></div>
  <div class="photo warm" role="img" aria-label="Iron club head resting on the grass" style="left:200px;top:0;width:54px;height:79px"></div>
  <div class="abs" style="left:145px;top:79px;width:109px;height:64px;background:var(--red);padding:16px 16px">
    <div class="w" style="font-size:5px;font-weight:600;line-height:1.1">Enter your<br><span class="lt">best title here</span></div>
    <div class="txt w" style="margin-top:2px;color:#fbdcdc">Lorem Ipsum is simply dummy text of the printing and typesetting industry.</div>
  </div>
  <div class="foot"><b>2022</b> All right Reserved</div><div class="pg" style="color:#f6c">18</div>
</section>

<!-- 19 Contact -->
<section class="slide" style="left:616px;top:696px">
  <div class="side"><div class="menu"><i style="top:3px"></i><i style="top:5px"></i><i style="top:7px"></i></div><div class="brand"><span>GreenGlider</span><b></b></div></div>
  <div class="photo map" role="img" aria-label="Folded street map" style="left:65px;top:0;width:189px;height:143px;clip-path:polygon(0 0,100% 0,100% 100%,40% 100%,60% 70%)"></div>
  <svg class="abs" style="left:100px;top:78px" width="154" height="65"><polygon points="0,65 60,0 90,65" fill="#2c3548"/></svg>
  <div class="abs" style="left:133px;top:68px;width:43px;height:25px;background:#222;border-radius:2px;padding:3px 4px">
    <div class="red" style="font-size:2.5px">Address Detail</div>
    <div class="txt w" style="font-size:2.3px;color:#ccc">Lorem Ipsum is simply dummy text of the printing and typesetting industry.</div>
  </div>
  <div class="abs sub" style="left:19px;top:33px">Your best sub title</div>
  <div class="abs h" style="left:19px;top:40px">Get in touch</div>
  <div class="abs txt" style="left:19px;top:52px;width:83px"><b style="color:#222">Ut wisi enim</b> ad minim veniam, quis nostrud exerci tation ullamcorper nibh euismod tincidunt ut laoreet dolore magna aliquam erat volutpat. Ut wisi enim ad minim veniam, quis nostrud exerci tation ullamcorper nibh euismod tincidunt ut laoreet</div>
  <div class="abs" style="left:20px;top:93px;display:grid;grid-template-columns:46px 46px;row-gap:7px;font-size:2.8px;color:#666">
    <div><span style="display:inline-block;width:4.5px;height:4.5px;border:.6px solid var(--red);vertical-align:middle;margin-right:3px"></span>@GreenGlider</div>
    <div><span style="display:inline-block;width:4.5px;height:4.5px;border:.6px solid var(--red);vertical-align:middle;margin-right:3px"></span>@GreenGlider</div>
    <div><span style="display:inline-block;width:4.5px;height:4.5px;border:.6px solid var(--red);vertical-align:middle;margin-right:3px"></span>@GreenGlider</div>
    <div><span style="display:inline-block;width:4.5px;height:4.5px;border:.6px solid var(--red);vertical-align:middle;margin-right:3px"></span>@GreenGlider</div>
  </div>
  <div class="foot"><b>2022</b> All right Reserved</div>
</section>

<!-- 20 Thank you -->
<section class="slide" style="left:901px;top:696px">
  <div class="side"><div class="menu"><i style="top:3px"></i><i style="top:5px"></i><i style="top:7px"></i></div><div class="brand"><span>GreenGlider</span><b></b></div></div>
  <svg class="abs" style="left:0;top:0" width="254" height="143"><polygon points="173,0 254,0 254,143 95,143" fill="#111"/></svg>
  <div class="photo rust" role="img" aria-label="Wedge club head resting behind a golf ball in warm light" style="left:26px;top:24px;width:202px;height:94px"></div>
  <svg class="abs" style="left:203px;top:94px" width="25" height="24"><polygon points="25,0 25,24 0,24" fill="#d71920"/></svg>
  <div class="abs w" style="left:26px;width:202px;top:59px;text-align:center;font-size:13px;font-weight:600">Thank <span style="color:var(--red)">You</span></div>
  <div class="abs txt w" style="left:86px;width:82px;top:77px;text-align:center;color:#f2dcd6">Lorem Ipsum is simply dummy text of the printing and typesetting industry.</div>
  <div class="abs" style="left:203px;top:128px;display:flex;gap:1.5px">
    <i style="width:5px;height:5px;border:.5px solid var(--red)"></i><i style="width:5px;height:5px;border:.5px solid var(--red)"></i><i style="width:5px;height:5px;border:.5px solid var(--red)"></i><i style="width:5px;height:5px;border:.5px solid var(--red)"></i>
  </div>
</section>

</body>
</html>
```